Ferrowave.com website design

I need a basic website for www.ferrowave.com. Ferro Wave has been hosting websites since 2002 via partnership arrangement with Stackhollow.com and Namequarry.com. We do not do any design, only hosting for small companies and nonprofits. We are referring people to PixelGuild and others to get their websites developed. Our website and pricing does not change often, but I need to be able to easily update the pricing and contact page.

Target Market(s)

Small company and non profit organizations

Industry/Entity Type

Utility

Coding

Coded - Design and coding required

Number of Pages Required

5+ page

Colors

Designer to choose colors to be used in the design.

Requirements
Must have
• Wordsmith format for easy content management. The logo attached. Contact us page with the following: Phone and fax are the same number: 888.514.2973. Email address is myferrowave@mailnest.example. Mailing address is 4819 E. Tolliver Bend #317, Searcy, AR 72143.
Nice to have
• Some kind of badge or tag line on the home page that celebrates our 15th year of hosting without a single hosting without any downtime. We are are 15 year partners with Stackhollow.com and Namequarry.com. Website Design tab needs to reference PixelGuild or others for all their website design needs. We provide no design or updating services. We will provide the developers FTP access to our dedicated Linux server. We do not provide email services other than redirects to their proprietary email or gmail, yahoo, etc. Needs a services and pricing tab. We provide domain registration services via our partnership with Namequarry.com. We will want a way for them to submit a suggested domain name for us to verify if available. I might be able to get a link from Namequarry.com to our account for you to include on that tab REGISTER DOMAIN. The tab buttons can be: WHO WE ARE, WHAT WE DO, WHEN YOU NEED US, WHERE TO REACH US. Maybe consider making the WHO, WHAT, WHEN and WHERE a dark blue color the rest of the text different color just so they stand out
Should not have
• A lot of animation that takes a long time to open. Clean and simple website.

```html
<!DOCTYPE html>
<html lang="en">
<head>
<meta charset="utf-8">
<title>Ferro Wave – Website Hosting</title>
<link rel="stylesheet" href="https://fonts.googleapis.com/css2?family=Source+Sans+3:ital,wght@0,400;0,600;0,700;1,400&display=swap">
<style>
:root{
  --blue:#3a8fd1;
  --blue-light:#62b1ec;
  --navy:#0d3a66;
  --navy-2:#0f4a86;
  --ink:#111820;
  --nav-ink:#16406b;
  --muted:#8a96a3;
  --grey-head:#a9aeb3;
  --line:#e4e8ec;
  --stripe:#f1f2f3;
  --sky:#deeefa;
  --white:#ffffff;
}
*{box-sizing:border-box;margin:0;padding:0}
html,body{width:1200px;height:2497px;overflow:hidden}
body{font-family:"Source Sans 3",Arial,sans-serif;color:var(--ink);background:var(--white);position:relative}
section,header,footer,.topbar{position:absolute;left:0;width:1200px}
a{color:inherit;text-decoration:none}

/* top bar */
.topbar{top:0;height:37px;background:var(--blue);color:var(--white);font-size:11px}
.topbar ul{list-style:none;display:flex;gap:22px;position:absolute;right:260px;top:11px}
.topbar li{display:flex;align-items:center;gap:6px}
.topbar svg{width:11px;height:11px}

/* header */
.site-header{top:37px;height:81px;border-bottom:1px solid var(--line)}
.brand{position:absolute;left:245px;top:12px;display:flex;align-items:center;gap:8px}
.brand-mark{width:54px;height:54px;background:var(--blue);border-radius:4px}
.brand-name{font-size:20px;font-weight:700;color:var(--navy);letter-spacing:.3px;line-height:1}
.brand-sub{font-size:8px;color:var(--muted);letter-spacing:1.5px;margin-top:3px}
.main-nav{position:absolute;right:243px;top:29px;display:flex;gap:27px;font-size:11px;font-weight:600;color:var(--nav-ink)}
.main-nav svg{width:13px;height:12px}

/* hero */
.hero{top:118px;height:381px}
.hero-art{position:absolute;left:266px;top:48px;width:258px;height:242px;border-radius:14px;
  background:linear-gradient(160deg,#e8f6fc 0%,#bfe6f5 55%,#f7c9c0 100%)}
.hero-copy{position:absolute;left:609px;top:66px;width:300px}
.hero-copy h1{font-size:19px;font-weight:700;line-height:1.25}
.hero-copy p{font-size:11px;line-height:1.45;color:#3b4652;margin-top:18px}
.btn{display:inline-block;font-size:11px;text-align:center;border-radius:2px}
.btn-solid{background:var(--blue-light);color:var(--white)}
.btn-line{border:1px solid var(--blue-light);color:#3b4652;background:var(--white)}
.hero-actions{margin-top:20px;display:flex;gap:10px}
.hero-actions .btn{width:108px;height:31px;line-height:30px}
.arrow{position:absolute;width:15px;height:15px;background:var(--blue);border-radius:2px;display:flex;align-items:center;justify-content:center}
.arrow svg{width:7px;height:7px}
.dots{position:absolute;display:flex;gap:4px;left:50%;transform:translateX(-50%)}
.dots span{width:7px;height:7px;border-radius:50%;border:1px solid var(--blue)}
.dots span.on{background:var(--blue)}

/* domain band */
.domain-band{top:499px;height:218px}
.domain-search,.create-site{position:absolute;top:0;height:218px;color:var(--white)}
.domain-search{left:0;width:599px;background:var(--navy)}
.create-site{left:599px;width:601px;background:var(--navy-2)}
.band-title{font-size:18px;font-weight:700;position:absolute;top:46px}
.band-sub{font-size:8px;opacity:.85;position:absolute;top:72px}
.domain-search .band-title,.domain-search .band-sub{left:62px}
.search-row{position:absolute;left:62px;top:103px;display:flex;gap:3px}
.search-row .field{width:365px;height:31px;background:var(--white);border-radius:2px;color:#b4bcc4;font-size:11px;padding:9px 12px}
.search-row .btn{width:109px;height:31px;line-height:31px}
.tlds{position:absolute;left:62px;top:149px;display:flex;gap:22px;font-size:9px}
.tlds span{display:flex;align-items:center;gap:8px}
.tlds i{width:13px;height:13px;background:var(--white);border-radius:2px;display:block}
.create-site .band-title,.create-site .band-sub{left:72px}
.partner-row{position:absolute;left:72px;top:100px;display:flex;gap:22px;align-items:center;font-size:15px;font-weight:600}
.partner-row .dot{display:inline-block;width:9px;height:9px;border-radius:50%;background:var(--white);margin-right:5px}
.create-site .btn{position:absolute;left:72px;top:140px;width:110px;height:31px;line-height:31px}

/* section heads */
.section-head{text-align:center}
.section-head h2{font-size:27px;font-weight:700}
.section-head p{font-size:11px;color:var(--blue);margin-top:4px}

/* packages */
.packages{top:717px;height:581px;border-bottom:1px solid var(--line)}
.packages .section-head{position:absolute;top:51px;width:100%}
.plans{position:absolute;left:245px;top:160px;width:695px;height:343px;border:1px solid var(--line);display:flex}
.plan{width:174px;position:relative;text-align:center}
.plan + .plan{border-left:1px solid var(--line)}
.plan.featured{border:1px solid var(--blue);border-radius:2px;margin-top:-17px;height:377px;background:var(--white);z-index:1}
.plan h3{font-size:18px;font-weight:700;color:var(--grey-head);margin-top:4px}
.plan.featured h3{margin-top:21px}
.plan-icon{width:28px;height:28px;margin:8px auto 0;display:block}
.price{font-size:11px;font-weight:700;color:var(--navy);margin-top:6px}
.price-note{font-size:8px;color:#b4bcc4;margin-top:4px}
.features{list-style:none;margin-top:41px;text-align:left}
.features li{height:25px;font-size:8px;color:#6b7682;display:flex;align-items:center;gap:10px;padding-left:10px}
.features li:nth-child(odd){background:var(--stripe)}
.features svg{width:11px;height:11px;flex:none}
.plan .btn{width:108px;height:31px;line-height:30px;margin-top:6px}

/* services */
.services{top:1298px;height:452px}
.services .section-head{position:absolute;top:64px;width:100%}
.service{position:absolute;top:178px;width:212px;text-align:center}
.service-art{width:92px;height:82px;margin:0 auto;border-radius:10px;background:linear-gradient(135deg,#dbe6ef,#9fcdef)}
.service h3{font-size:18px;font-weight:600;margin-top:30px}
.service p{font-size:9.5px;line-height:1.5;color:#55606b;margin-top:10px}

/* clients */
.clients{top:1750px;height:377px;background:var(--sky)}
.clients .section-head{position:absolute;top:38px;width:100%}
.quote-card{position:absolute;top:140px;width:347px;height:157px;background:var(--white);box-shadow:0 2px 5px rgba(0,0,0,.12);padding:20px 20px 0 20px}
.quote-badge{position:absolute;left:17px;top:-8px;width:24px;height:24px;border-radius:50%;background:var(--blue);display:flex;align-items:center;justify-content:center;color:var(--white);font-size:16px;font-weight:700;line-height:1}
.quote-card blockquote{font-size:9.5px;font-style:italic;color:#8a949e;line-height:1.5}
.quote-card .who{font-size:9px;font-weight:700;margin-top:18px}
.quote-card .role{font-size:7.5px;color:#55606b}

/* partner names */
.logo-strip{top:2127px;height:113px;display:flex;justify-content:center;align-items:center;gap:38px;font-weight:700;color:var(--ink)}
.logo-strip span{font-size:16px;display:flex;align-items:center;gap:5px}
.logo-strip span.big{font-size:21px}
.logo-strip i{width:9px;height:9px;border-radius:50%;background:var(--ink);display:block}

/* footer */
.site-footer{top:2240px;height:257px;background:var(--blue);color:var(--white)}
.foot-col{position:absolute;top:56px;font-size:9px}
.foot-col h4{font-size:10px;font-weight:700;margin-bottom:18px}
.foot-col ul{list-style:none}
.foot-col li{margin-bottom:12px}
.foot-brand{left:245px;top:34px;width:170px}
.foot-mark{width:37px;height:37px;background:var(--white);border-radius:3px;margin-bottom:12px}
.foot-brand p{font-size:9px;font-weight:600;line-height:1.4}
.social{display:flex;gap:7px;margin-top:13px}
.social i{width:21px;height:21px;border:1px solid var(--white);border-radius:50%;display:block}
.copy{font-size:7.5px;margin-top:10px;line-height:1.55}
.contact li{display:flex;gap:6px;align-items:flex-start}
.contact svg{width:10px;height:10px;flex:none;margin-top:1px}
.send{display:block;width:110px;height:31px;line-height:29px;border:1.5px solid var(--white);border-radius:3px;text-align:center;font-size:10px;font-weight:700;margin-top:8px}
</style>
</head>
<body>

<div class="topbar">
  <ul>
    <li><svg viewBox="0 0 12 12"><path d="M3 1l2 2.5-1.2 1.3a7 7 0 003.4 3.4L8.5 7 11 9l-1 2C5 11 1 7 1 2z" fill="#fff"/></svg>888.514.2973</li>
    <li><svg viewBox="0 0 12 12"><rect x="1" y="2.5" width="10" height="7" fill="none" stroke="#fff"/><path d="M1 2.5l5 4 5-4" fill="none" stroke="#fff"/></svg>myferrowave@mailnest.example</li>
    <li><svg viewBox="0 0 12 12"><circle cx="6" cy="4" r="2.5" fill="none" stroke="#fff"/><path d="M1.5 11.5a4.5 4.5 0 019 0" fill="none" stroke="#fff"/></svg>User Login</li>
  </ul>
</div>

<header class="site-header">
  <div class="brand">
    <span class="brand-mark"></span>
    <div>
      <div class="brand-name">FERRO WAVE</div>
      <div class="brand-sub">WEBSITE HOSTING</div>
    </div>
  </div>
  <nav class="main-nav">
    <a>WHO</a><a>WHAT</a><a>WHEN</a><a>WHERE</a><a>CONTACT</a>
    <svg viewBox="0 0 14 12"><path d="M0 1h2.5l1.8 7h7.5L13 3H3.5" fill="none" stroke="#16406b" stroke-width="1.3"/><circle cx="5" cy="10.5" r="1" fill="#16406b"/><circle cx="11" cy="10.5" r="1" fill="#16406b"/></svg>
  </nav>
</header>

<section class="hero">
  <div class="arrow" style="left:62px;top:170px"><svg viewBox="0 0 8 8"><path d="M5.5 1L2.5 4l3 3" fill="none" stroke="#fff" stroke-width="1.4"/></svg></div>
  <div class="hero-art" role="img" aria-label="Illustration of a rocket launching from a desktop monitor with a light bulb and cloud"></div>
  <div class="hero-copy">
    <h1>Build yoyr first website<br>with super speed</h1>
    <p>Lorem ipsum dolor sit amet, consectetur adipisicing elit, sed do eiusmod tempor incididunt ut labore et dolore magna aliqua. Ut enim ad minim veniam, quis nostrud exercitation ullamco laboris nisi.</p>
    <div class="hero-actions">
      <a class="btn btn-solid">Get Started</a>
      <a class="btn btn-line">Check Price</a>
    </div>
  </div>
  <div class="arrow" style="left:1122px;top:170px"><svg viewBox="0 0 8 8"><path d="M2.5 1l3 3-3 3" fill="none" stroke="#fff" stroke-width="1.4"/></svg></div>
  <div class="dots" style="top:342px"><span class="on"></span><span></span><span></span></div>
</section>

<section class="domain-band">
  <div class="domain-search">
    <h2 class="band-title">Search your Domain</h2>
    <p class="band-sub">Lorem ipsum dolor sit amet, consectetur adipisicing elit</p>
    <div class="search-row">
      <div class="field">Your domain name</div>
      <a class="btn btn-solid">Search</a>
    </div>
    <div class="tlds"><span><i></i>.com</span><span><i></i>.net</span><span><i></i>.org</span><span><i></i>.in</span></div>
  </div>
  <div class="create-site">
    <h2 class="band-title">Create your Website</h2>
    <p class="band-sub">Lorem ipsum dolor sit amet, consectetur adipisicing elit</p>
    <div class="partner-row"><span><span class="dot"></span>PixelGuild</span><span>Ninetyplans</span><span>Gigharbor</span></div>
    <a class="btn btn-solid">Get started</a>
  </div>
</section>

<section class="packages">
  <div class="section-head"><h2>Our Packages</h2><p>Pay for what you use. no hidden charges</p></div>
  <div class="plans">
    <div class="plan">
      <h3>Personal</h3>
      <svg class="plan-icon" viewBox="0 0 28 28"><circle cx="14" cy="7" r="4" fill="none" stroke="#16406b" stroke-width="1.5"/><path d="M9 26v-9a5 5 0 0110 0v9" fill="none" stroke="#16406b" stroke-width="1.5"/></svg>
      <div class="price">$3/ Month</div><div class="price-note">Lorem ipsum dolor sit amet</div>
      <ul class="features">
        <li><svg viewBox="0 0 11 11"><rect x=".5" y="1.5" width="8" height="8" fill="none" stroke="#16406b"/><path d="M2.5 5l2 2L10 1" fill="none" stroke="#16406b" stroke-width="1.3"/></svg>Lorem ipsum dolor sit amet</li>
        <li><svg viewBox="0 0 11 11"><rect x=".5" y="1.5" width="8" height="8" fill="none" stroke="#16406b"/><path d="M2.5 5l2 2L10 1" fill="none" stroke="#16406b" stroke-width="1.3"/></svg>Lorem ipsum dolor sit amet</li>
        <li><svg viewBox="0 0 11 11"><rect x=".5" y="1.5" width="8" height="8" fill="none" stroke="#16406b"/><path d="M2.5 5l2 2L10 1" fill="none" stroke="#16406b" stroke-width="1.3"/></svg>Lorem ipsum dolor sit amet</li>
        <li><svg viewBox="0 0 11 11"><rect x=".5" y="1.5" width="8" height="8" fill="none" stroke="#16406b"/><path d="M2.5 5l2 2L10 1" fill="none" stroke="#16406b" stroke-width="1.3"/></svg>Lorem ipsum dolor sit amet</li>
        <li><svg viewBox="0 0 11 11"><rect x=".5" y="1.5" width="8" height="8" fill="none" stroke="#16406b"/><path d="M2.5 5l2 2L10 1" fill="none" stroke="#16406b" stroke-width="1.3"/></svg>Lorem ipsum dolor sit amet</li>
        <li><svg viewBox="0 0 11 11"><rect x=".5" y="1.5" width="8" height="8" fill="none" stroke="#16406b"/><path d="M2.5 5l2 2L10 1" fill="none" stroke="#16406b" stroke-width="1.3"/></svg>Lorem ipsum dolor sit amet</li>
      </ul>
      <a class="btn btn-line">Buy now</a>
    </div>
    <div class="plan featured">
      <h3>Professional</h3>
      <svg class="plan-icon" viewBox="0 0 28 28"><circle cx="9" cy="8" r="3" fill="none" stroke="#16406b" stroke-width="1.5"/><circle cx="19" cy="8" r="3" fill="none" stroke="#16406b" stroke-width="1.5"/><path d="M5 24v-7a4 4 0 018 0v7M15 24v-7a4 4 0 018 0v7" fill="none" stroke="#16406b" stroke-width="1.5"/></svg>
      <div class="price">$9/ Month</div><div class="price-note">Lorem ipsum dolor sit amet</div>
      <ul class="features">
        <li><svg viewBox="0 0 11 11"><rect x=".5" y="1.5" width="8" height="8" fill="none" stroke="#16406b"/><path d="M2.5 5l2 2L10 1" fill="none" stroke="#16406b" stroke-width="1.3"/></svg>Lorem ipsum dolor sit amet</li>
        <li><svg viewBox="0 0 11 11"><rect x=".5" y="1.5" width="8" height="8" fill="none" stroke="#16406b"/><path d="M2.5 5l2 2L10 1" fill="none" stroke="#16406b" stroke-width="1.3"/></svg>Lorem ipsum dolor sit amet</li>
        <li><svg viewBox="0 0 11 11"><rect x=".5" y="1.5" width="8" height="8" fill="none" stroke="#16406b"/><path d="M2.5 5l2 2L10 1" fill="none" stroke="#16406b" stroke-width="1.3"/></svg>Lorem ipsum dolor sit amet</li>
        <li><svg viewBox="0 0 11 11"><rect x=".5" y="1.5" width="8" height="8" fill="none" stroke="#16406b"/><path d="M2.5 5l2 2L10 1" fill="none" stroke="#16406b" stroke-width="1.3"/></svg>Lorem ipsum dolor sit amet</li>
        <li><svg viewBox="0 0 11 11"><rect x=".5" y="1.5" width="8" height="8" fill="none" stroke="#16406b"/><path d="M2.5 5l2 2L10 1" fill="none" stroke="#16406b" stroke-width="1.3"/></svg>Lorem ipsum dolor sit amet</li>
        <li><svg viewBox="0 0 11 11"><rect x=".5" y="1.5" width="8" height="8" fill="none" stroke="#16406b"/><path d="M2.5 5l2 2L10 1" fill="none" stroke="#16406b" stroke-width="1.3"/></svg>Lorem ipsum dolor sit amet</li>
      </ul>
      <a class="btn btn-solid">Buy Now</a>
    </div>
    <div class="plan">
      <h3>Company</h3>
      <svg class="plan-icon" viewBox="0 0 28 28"><path d="M3 13L14 4l11 9M6 11v14h16V11" fill="none" stroke="#16406b" stroke-width="1.5"/><rect x="11" y="16" width="6" height="9" fill="none" stroke="#16406b" stroke-width="1.5"/></svg>
      <div class="price">$15/ Month</div><div class="price-note">Lorem ipsum dolor sit amet</div>
      <ul class="features">
        <li><svg viewBox="0 0 11 11"><rect x=".5" y="1.5" width="8" height="8" fill="none" stroke="#16406b"/><path d="M2.5 5l2 2L10 1" fill="none" stroke="#16406b" stroke-width="1.3"/></svg>Lorem ipsum dolor sit amet</li>
        <li><svg viewBox="0 0 11 11"><rect x=".5" y="1.5" width="8" height="8" fill="none" stroke="#16406b"/><path d="M2.5 5l2 2L10 1" fill="none" stroke="#16406b" stroke-width="1.3"/></svg>Lorem ipsum dolor sit amet</li>
        <li><svg viewBox="0 0 11 11"><rect x=".5" y="1.5" width="8" height="8" fill="none" stroke="#16406b"/><path d="M2.5 5l2 2L10 1" fill="none" stroke="#16406b" stroke-width="1.3"/></svg>Lorem ipsum dolor sit amet</li>
        <li><svg viewBox="0 0 11 11"><rect x=".5" y="1.5" width="8" height="8" fill="none" stroke="#16406b"/><path d="M2.5 5l2 2L10 1" fill="none" stroke="#16406b" stroke-width="1.3"/></svg>Lorem ipsum dolor sit amet</li>
        <li><svg viewBox="0 0 11 11"><rect x=".5" y="1.5" width="8" height="8" fill="none" stroke="#16406b"/><path d="M2.5 5l2 2L10 1" fill="none" stroke="#16406b" stroke-width="1.3"/></svg>Lorem ipsum dolor sit amet</li>
        <li><svg viewBox="0 0 11 11"><rect x=".5" y="1.5" width="8" height="8" fill="none" stroke="#16406b"/><path d="M2.5 5l2 2L10 1" fill="none" stroke="#16406b" stroke-width="1.3"/></svg>Lorem ipsum dolor sit amet</li>
      </ul>
      <a class="btn btn-line">Buy now</a>
    </div>
    <div class="plan">
      <h3>Pro</h3>
      <svg class="plan-icon" viewBox="0 0 28 28"><circle cx="14" cy="14" r="11" fill="#d8ecf9" stroke="#16406b" stroke-width="1.5"/><path d="M3 14h22M14 3c-4 4-4 18 0 22M14 3c4 4 4 18 0 22" fill="none" stroke="#16406b" stroke-width="1.2"/></svg>
      <div class="price">$30/ Month</div><div class="price-note">Lorem ipsum dolor sit amet</div>
      <ul class="features">
        <li><svg viewBox="0 0 11 11"><rect x=".5" y="1.5" width="8" height="8" fill="none" stroke="#16406b"/><path d="M2.5 5l2 2L10 1" fill="none" stroke="#16406b" stroke-width="1.3"/></svg>Lorem ipsum dolor sit amet</li>
        <li><svg viewBox="0 0 11 11"><rect x=".5" y="1.5" width="8" height="8" fill="none" stroke="#16406b"/><path d="M2.5 5l2 2L10 1" fill="none" stroke="#16406b" stroke-width="1.3"/></svg>Lorem ipsum dolor sit amet</li>
        <li><svg viewBox="0 0 11 11"><rect x=".5" y="1.5" width="8" height="8" fill="none" stroke="#16406b"/><path d="M2.5 5l2 2L10 1" fill="none" stroke="#16406b" stroke-width="1.3"/></svg>Lorem ipsum dolor sit amet</li>
        <li><svg viewBox="0 0 11 11"><rect x=".5" y="1.5" width="8" height="8" fill="none" stroke="#16406b"/><path d="M2.5 5l2 2L10 1" fill="none" stroke="#16406b" stroke-width="1.3"/></svg>Lorem ipsum dolor sit amet</li>
        <li><svg viewBox="0 0 11 11"><rect x=".5" y="1.5" width="8" height="8" fill="none" stroke="#16406b"/><path d="M2.5 5l2 2L10 1" fill="none" stroke="#16406b" stroke-width="1.3"/></svg>Lorem ipsum dolor sit amet</li>
        <li><svg viewBox="0 0 11 11"><rect x=".5" y="1.5" width="8" height="8" fill="none" stroke="#16406b"/><path d="M2.5 5l2 2L10 1" fill="none" stroke="#16406b" stroke-width="1.3"/></svg>Lorem ipsum dolor sit amet</li>
      </ul>
      <a class="btn btn-line">Buy now</a>
    </div>
  </div>
</section>

<section class="services">
  <div class="section-head"><h2>Our Services</h2><p>Pay for what you use. no hidden charges</p></div>
  <div class="service" style="left:248px">
    <div class="service-art" role="img" aria-label="Icon of two interlocking gears"></div>
    <h3>Easy to Customise</h3>
    <p>Lorem ipsum dolor sit amet, consectetur adipisicing elit, sed do eiusmod tempor incididunt ut labore et dolore magna aliqua. Ut enim ad minim veniam, quis nostrud exercitation ullamco.</p>
  </div>
  <div class="service" style="left:495px">
    <div class="service-art" role="img" aria-label="Icon of a rocket launching from a monitor"></div>
    <h3>99% Uptime</h3>
    <p>Lorem ipsum dolor sit amet, consectetur adipisicing elit, sed do eiusmod tempor incididunt ut labore et dolore magna aliqua. Ut enim ad minim veniam, quis nostrud exercitation ullamco.</p>
  </div>
  <div class="service" style="left:738px">
    <div class="service-art" role="img" aria-label="Icon of two hands reaching to each other"></div>
    <h3>Easy alltime Support</h3>
    <p>Lorem ipsum dolor sit amet, consectetur adipisicing elit, sed do eiusmod tempor incididunt ut labore et dolore magna aliqua. Ut enim ad minim veniam, quis nostrud exercitation ullamco.</p>
  </div>
</section>

<section class="clients">
  <div class="section-head"><h2>Our Clients</h2><p>Pay for what you use. no hidden charges</p></div>
  <div class="arrow" style="left:206px;top:213px"><svg viewBox="0 0 8 8"><path d="M5.5 1L2.5 4l3 3" fill="none" stroke="#fff" stroke-width="1.4"/></svg></div>
  <article class="quote-card" style="left:245px">
    <span class="quote-badge">&ldquo;</span>
    <blockquote>Lorem ipsum dolor sit amet, consectetur adipisicing elit, sed do eiusmod tempor incididunt ut labore et dolore magna aliqua. Ut enim ad minim veniam, quis nostrud exercitation ullamco laboris nisi ut aliquip ex ea commodo consequat. Duis aute irure dolor in reprehenderit in voluptate velit esse cillum dolore</blockquote>
    <div class="who">Marcus Hale</div><div class="role">Ceo &amp; Admin</div>
  </article>
  <article class="quote-card" style="left:611px">
    <span class="quote-badge">&ldquo;</span>
    <blockquote>Lorem ipsum dolor sit amet, consectetur adipisicing elit, sed do eiusmod tempor incididunt ut labore et dolore magna aliqua. Ut enim ad minim veniam, quis nostrud exercitation ullamco laboris nisi ut aliquip ex ea commodo consequat. Duis aute irure dolor in reprehenderit in voluptate velit esse cillum dolore</blockquote>
    <div class="who">Owen Price</div><div class="role">Ceo &amp; Admin</div>
  </article>
  <div class="arrow" style="left:978px;top:213px"><svg viewBox="0 0 8 8"><path d="M2.5 1l3 3-3 3" fill="none" stroke="#fff" stroke-width="1.4"/></svg></div>
  <div class="dots" style="top:333px"><span class="on"></span><span></span><span></span></div>
</section>

<section class="logo-strip">
  <span><i></i>PixelGuild</span>
  <span>Ninetyplans</span>
  <span class="big">Gigharbor</span>
  <span class="big">Stackhollow</span>
  <span class="big">Namequarry.com</span>
</section>

<footer class="site-footer">
  <div class="foot-col foot-brand">
    <div class="foot-mark"></div>
    <p>Lorem ipsum dolor sit amet, consectetur adipisicing elit, sed do eiusmod tempor incididunt ut labore et dolore magna aliqua. Ut enim ad minim veniam, quis nostrud exercitation</p>
    <div class="social"><i></i><i></i><i></i><i></i></div>
    <p class="copy">© 2017 Ferro Wave.<br>All rights reserved.</p>
  </div>
  <div class="foot-col" style="left:426px">
    <h4>Important Links</h4>
    <ul><li>Support</li><li>Privacy</li><li>Terms &amp; Conditions</li><li>Dedicated Servers</li></ul>
  </div>
  <div class="foot-col" style="left:609px">
    <h4>Our Partners</h4>
    <ul><li>Namequarry.com</li><li>Stackhollow</li><li>Ninetyplans</li><li>PixelGuild</li><li>Gigharbor</li></ul>
  </div>
  <div class="foot-col contact" style="left:792px">
    <h4>Contact US</h4>
    <ul>
      <li><svg viewBox="0 0 12 12"><path d="M3 1l2 2.5-1.2 1.3a7 7 0 003.4 3.4L8.5 7 11 9l-1 2C5 11 1 7 1 2z" fill="#fff"/></svg>888.514.2973</li>
      <li><svg viewBox="0 0 12 12"><rect x="1" y="2.5" width="10" height="7" fill="none" stroke="#fff"/><path d="M1 2.5l5 4 5-4" fill="none" stroke="#fff"/></svg>myferrowave@mailnest.example</li>
      <li><svg viewBox="0 0 12 12"><path d="M11 1L1 5.5l4.5 1.5L7 11z" fill="none" stroke="#fff"/></svg><span>4819 E. Tolliver Bend #317,<br>Millbrook Falls, AR 72990</span></li>
    </ul>
    <a class="send">Send Message</a>
  </div>
</footer>

</body>
</html>
```